Art for parenting podcast with straight/direct talk...no fluff here! "Plain Word for Families"

I need an image that will not look fluffy or soft. A no-nonsense look. This is not a 'I love parenting' podcast. It is for frustrated parents who don't know what to do. The name is 'Plain Word for Families'. The design should, therefore, NOT have hearts and flowers but, instead, look clean and direct. My logo has shades of blue so that would be nice. I have done this work for over 30 years and am well-degreed so would like the design to look stable/established. I have attached my company's logo.

Target Market(s)

Frustrated parents of children - age birth to 20

Industry/Entity Type

Coaching/Counseling for parents

Font styles to use
Serif
Sans Serif

Colors
0054AA
0677BA
7BADD7
CADEEF
E8F1F8

Requirements
Must have
• A look that is clean/bold/direct and professional. Serious.
Nice to have
• If it looks good, my name with my degrees behind my name. MS, MEd. Another thought would be to have a background image of a frustrated parent. Not sure if that would be good or look too busy.
Should not have
• Flowers, fluff, soft appearance, pinks, light colors

```html
<!DOCTYPE html>
<html lang="en">
<head>
<meta charset="utf-8">
<title>Plain Word for Families — Podcast</title>
<link rel="stylesheet" href="https://fonts.googleapis.com/css2?family=Anton&family=Oswald:wght@300;500;600&display=swap">
<style>
  :root {
    --navy-deep: #06264f;
    --navy: #0b3a70;
    --brand-blue: #0054aa;
    --mid-blue: #0677ba;
    --bright-blue: #1c8fd6;
    --sky: #7badd7;
    --mist: #cadeef;
    --white: #ffffff;
  }
  html, body {
    margin: 0;
    padding: 0;
    width: 1200px;
    height: 1200px;
    overflow: hidden;
    background: var(--navy-deep);
  }
  .cover {
    position: relative;
    width: 1200px;
    height: 1200px;
    overflow: hidden;
    background: var(--navy-deep);
  }
  .photo {
    position: absolute;
  }
  .photo--mother {
    left: 0; top: 0; width: 640px; height: 624px;
    background:
      radial-gradient(ellipse 22% 30% at 52% 42%, rgba(40,130,200,0.85) 0%, rgba(24,100,170,0.6) 55%, rgba(24,100,170,0) 100%),
      radial-gradient(ellipse 40% 62% at 50% 48%, #17599a 0%, #0f4681 50%, rgba(6,38,79,0) 100%),
      radial-gradient(ellipse 60% 90% at 45% 30%, #0d3a70 0%, var(--navy-deep) 100%);
  }
  .photo--father {
    left: 600px; top: 0; width: 600px; height: 418px;
    background:
      radial-gradient(ellipse 22% 40% at 62% 48%, rgba(44,140,210,0.9) 0%, rgba(28,110,180,0.5) 60%, rgba(28,110,180,0) 100%),
      radial-gradient(ellipse 16% 30% at 92% 30%, rgba(40,130,200,0.75) 0%, rgba(40,130,200,0) 100%),
      radial-gradient(ellipse 14% 26% at 28% 40%, rgba(40,130,200,0.6) 0%, rgba(40,130,200,0) 100%),
      linear-gradient(90deg, #0a3264 0%, #0d447e 55%, #1467ad 100%);
  }
  .photo--child {
    left: 0; top: 624px; width: 1200px; height: 576px;
    background:
      radial-gradient(ellipse 20% 55% at 50% 55%, rgba(36,124,196,0.85) 0%, rgba(24,100,170,0.5) 60%, rgba(24,100,170,0) 100%),
      radial-gradient(ellipse 34% 80% at 50% 60%, #165a9c 0%, #10498a 45%, #0a3366 100%);
  }
  .title-band {
    position: absolute;
    left: 0; top: 433px; width: 1200px; height: 191px;
    background: linear-gradient(90deg, rgba(4,30,64,0.35) 0%, rgba(4,30,64,0.55) 60%, rgba(4,30,64,0.45) 100%);
  }
  .rule {
    position: absolute;
    height: 15px;
  }
  .rule--upper {
    left: 230px; top: 418px; width: 970px;
    background: linear-gradient(90deg, rgba(6,119,186,0) 0%, var(--mid-blue) 30%, var(--mid-blue) 100%);
  }
  .rule--lower {
    left: 0; top: 986px; width: 1095px;
    background: linear-gradient(90deg, var(--mid-blue) 0%, var(--mid-blue) 70%, rgba(6,119,186,0) 100%);
  }
  .brand {
    position: absolute;
    left: 0; top: 196px; width: 1200px;
    display: flex;
    flex-direction: column;
    align-items: center;
    gap: 22px;
  }
  .brand__dot {
    width: 96px; height: 96px;
    border-radius: 50%;
    background: var(--bright-blue);
  }
  .brand__name {
    font-family: "Oswald", sans-serif;
    font-weight: 600;
    font-size: 50px;
    letter-spacing: 2px;
    text-transform: uppercase;
    color: var(--sky);
    line-height: 1;
  }
  .title {
    position: absolute;
    left: 0; top: 428px;
    width: 1200px;
    margin: 0;
    font-family: "Anton", sans-serif;
    font-weight: 400;
    font-size: 172px;
    line-height: 164px;
    letter-spacing: 2px;
    color: var(--white);
    text-transform: uppercase;
  }
  .title__line {
    display: block;
    white-space: nowrap;
  }
  .title__line--first { padding-left: 186px; }
  .title__line--second { padding-left: 200px; }
  .format {
    position: absolute;
    left: 160px; top: 1012px;
    width: 896px;
    display: flex;
    justify-content: space-between;
    font-family: "Oswald", sans-serif;
    font-weight: 300;
    font-size: 146px;
    line-height: 146px;
    color: var(--white);
    text-transform: uppercase;
  }
</style>
</head>
<body>
  <main class="cover">
    <div class="photo photo--mother" role="img" aria-label="Photo of a frustrated mother frowning, toned in blue"></div>
    <div class="photo photo--father" role="img" aria-label="Photo of an exasperated father shouting with raised hands, toned in blue"></div>
    <div class="photo photo--child" role="img" aria-label="Photo of a scowling boy looking up, toned in blue"></div>

    <div class="title-band"></div>
    <div class="rule rule--upper"></div>
    <div class="rule rule--lower"></div>

    <div class="brand">
      <span class="brand__dot"></span>
      <span class="brand__name">Steadyhand Parenting</span>
    </div>

    <h1 class="title">
      <span class="title__line title__line--first">Plain Word</span>
      <span class="title__line title__line--second">For Families</span>
    </h1>

    <div class="format" aria-label="Podcast">
      <span>P</span><span>O</span><span>D</span><span>C</span><span>A</span><span>S</span><span>T</span>
    </div>
  </main>
</body>
</html>
```